need corporate, modern business card created for Consulting Company

I need a slick business card using elements from my website, as well as, integrating my pixelforge-created logo (see files).

The business card needs to be:
1. Corporate and modern
2. Clean and professional

I've included a PSD with the logo/icon that you can use to create it. Feel free to try a metallic finish on the logo, make it bigger/small, underlay it. Whatever you need to do to make my card stand out.

Try a black background, or white background or gray.

The idea is for my card to be memorable as well as professional and corporate.

Target Market(s)

Corporate business in the US and Canada.

Industry/Entity Type

Business

Contact Information for Business Card

Enterprise Advancing Solutions
Martin Coble, Senior Partner
office: 1 877 555 0143
mobile: 1 519 555 0172
website: http://www.velmorant.com

Requirements
Must have
• Card-related information
• corporate, yet modern
• clean and professional
• incorporate the icon only
• must have an editable form when complete!
Nice to have
• metallic icon might be cool
• try it with white or black

```html
<!DOCTYPE html>
<html lang="en">
<head>
<meta charset="utf-8">
<title>Velmorant – Business Card</title>
<link rel="stylesheet" href="https://fonts.googleapis.com/css2?family=Comfortaa:wght@500;700&family=Oswald:wght@400;500&display=swap">
<style>
  :root {
    --backdrop: #121212;
    --card: #1c1c1d;
    --card-edge: #262628;
    --accent: #3a78c9;
    --text-light: #f2f2f2;
    --text-muted: #9a9a9c;
    --mark-grey: #b9b9bb;
  }
  * { box-sizing: border-box; margin: 0; padding: 0; }
  html, body {
    width: 1200px;
    height: 871px;
    overflow: hidden;
    background: var(--backdrop);
  }
  .canvas {
    position: relative;
    width: 1200px;
    height: 871px;
  }
  .card {
    position: absolute;
    background: linear-gradient(135deg, var(--card-edge) 0%, var(--card) 45%, var(--card) 100%);
    border-radius: 3px;
    box-shadow: 0 18px 40px rgba(0, 0, 0, 0.6);
    overflow: hidden;
  }

  /* Back of card */
  .card-back {
    left: 80px;
    top: 50px;
    width: 600px;
    height: 343px;
  }
  .card-back .brand {
    position: absolute;
    right: 40px;
    bottom: 40px;
    display: flex;
    align-items: center;
    gap: 12px;
  }
  .card-back .brand-square {
    width: 26px;
    height: 26px;
    background: var(--mark-grey);
  }
  .card-back .brand-name {
    font-family: "Comfortaa", sans-serif;
    font-weight: 700;
    font-size: 38px;
    color: var(--mark-grey);
    letter-spacing: 0.5px;
  }

  /* Front of card */
  .card-front {
    left: 420px;
    top: 430px;
    width: 700px;
    height: 400px;
  }
  .accent-bar {
    position: absolute;
    left: 120px;
    top: 0;
    width: 7px;
    height: 145px;
    background: var(--accent);
  }
  .holder {
    position: absolute;
    left: 150px;
    top: 40px;
  }
  .holder-name {
    font-family: "Comfortaa", sans-serif;
    font-weight: 500;
    font-size: 34px;
    color: var(--text-light);
    letter-spacing: 1px;
  }
  .holder-role {
    margin-top: 4px;
    font-family: "Oswald", sans-serif;
    font-size: 14px;
    color: var(--accent);
    letter-spacing: 2.5px;
  }
  .contacts {
    position: absolute;
    left: 40px;
    top: 205px;
    list-style: none;
  }
  .contacts li {
    display: flex;
    align-items: center;
    gap: 16px;
    font-family: "Oswald", sans-serif;
    font-weight: 500;
    font-size: 20px;
    color: var(--text-light);
    letter-spacing: 2px;
    line-height: 34px;
  }
  .contacts svg { width: 20px; height: 20px; fill: var(--accent); flex: none; }
  .brand-front {
    position: absolute;
    right: 60px;
    top: 120px;
    display: flex;
    align-items: center;
    gap: 14px;
  }
  .brand-front .brand-square {
    width: 30px;
    height: 30px;
    background: var(--accent);
  }
  .brand-front .brand-name {
    font-family: "Comfortaa", sans-serif;
    font-weight: 700;
    font-size: 48px;
    color: var(--text-light);
  }
  .website {
    position: absolute;
    right: 50px;
    bottom: 48px;
    display: flex;
    align-items: center;
    gap: 14px;
    font-family: "Oswald", sans-serif;
    font-size: 20px;
    color: var(--accent);
    letter-spacing: 4px;
  }
  .website svg { width: 22px; height: 22px; }
</style>
</head>
<body>
<main class="canvas">

  <section class="card card-back" aria-label="Card back">
    <div class="brand">
      <span class="brand-square"></span>
      <span class="brand-name">velmorant</span>
    </div>
  </section>

  <section class="card card-front" aria-label="Card front">
    <div class="accent-bar"></div>
    <div class="holder">
      <h1 class="holder-name">Martin Coble</h1>
      <p class="holder-role">Senior Partner</p>
    </div>

    <ul class="contacts">
      <li>
        <svg viewBox="0 0 20 20" aria-hidden="true"><path d="M2 6c0-2 3-3 8-3s8 1 8 3v1.5h-4V6H6v1.5H2z"/><rect x="4" y="9" width="12" height="8" rx="1.5"/></svg>
        1 877 555 0143
      </li>
      <li>
        <svg viewBox="0 0 20 20" aria-hidden="true"><path d="M6 1h8a1.5 1.5 0 0 1 1.5 1.5v15A1.5 1.5 0 0 1 14 19H6a1.5 1.5 0 0 1-1.5-1.5v-15A1.5 1.5 0 0 1 6 1zm0 2v12h8V3z"/></svg>
        1 519 555 0172
      </li>
      <li>
        <svg viewBox="0 0 20 20" aria-hidden="true"><path d="M1 4h18v12H1zm2 2v.5l7 5 7-5V6z"/></svg>
        info@velmorant.com
      </li>
    </ul>

    <div class="brand-front">
      <span class="brand-square"></span>
      <span class="brand-name">velmorant</span>
    </div>

    <div class="website">
      <svg viewBox="0 0 22 22" aria-hidden="true" fill="none" stroke="#3a78c9" stroke-width="1.8">
        <circle cx="11" cy="11" r="9"/>
        <ellipse cx="11" cy="11" rx="4" ry="9"/>
        <line x1="2" y1="11" x2="20" y2="11"/>
      </svg>
      www.velmorant.com
    </div>
  </section>

</main>
</body>
</html>
```